Sumworks.co.uk - front page and content page design
Site design for Sumworks.co.uk - a UK site hosting different calculators
Creative Brief
Internet Services
http://www.plotmeadow.co.uk
Project: Sumworks.co.uk
Idea: To host all of the different types of calculators on the site with supporting content
Our idea is generating targeted traffic through generic domains (we've got 4,500!). With Sumworks.co.uk, the domain will host loads of different calculators with content supporting the calculators on offer.
For Sumworks.co.uk, we'd like a design that is clean but colourful and allows us to colour the different sections of the site that we'll have. The initial premise is that we'll have sections for the different 'types' of calculators:
Health calculators
Finance calculators
Maths calculators
Conversion calculators
Pregnancy calculators
Within each section will be different calculators - so, for example, in Health, there will be a BMI calculator, BMR calculator and so on.
Ideally, we'd like each 'section' to have a different colour - i.e. blue for Health, green for Finance, blue for Maths, etc. The colours can be chosen by the designer as to what looks best.
We'd like a front page design and also a content page design. The home page shouldn't be too different in structure/layout to the content pages (i.e. structure follows through).
Ideally, there will be a column on the right hand side that allows advertising (300 x 250) and the main column for content should be at least 540px (this is where content and weidgets/calculators will be placed).
Once in a section, there should be a left menu that allows users to choose the type of calculator they want within that section.
This is our first try on Pixelgrove and we're hoping that if this works out, we can find some designer(s) through this who we can offer many more design projects as we have many generic domain names waiting to be designed.
Likes: Clean, colourful, elegant, professional
www.vitalpage.com
http://www.brightjotapp.com/tour/why-use-brightjot
http://www.kelvo.com/

```html
<!DOCTYPE html>
<html lang="en">
<head>
<meta charset="utf-8">
<title>Sumworks.co.uk – Tax Calculator</title>
<link rel="stylesheet" href="https://fonts.googleapis.com/css2?family=Arimo:ital,wght@0,400;0,700;1,700&display=swap">
<style>
  :root {
    --green: #7dc21e;
    --green-dark: #5c9a10;
    --green-pale: #d9efb8;
    --ink: #1c1c1c;
    --text: #333333;
    --muted: #666666;
    --panel: #e4e4e4;
    --panel-line: #c9c9c9;
    --white: #ffffff;
    --search: #d6d6d6;
    --ad-dark: #161616;
    --social: #8a8f99;
  }
  * { box-sizing: border-box; margin: 0; padding: 0; }
  html, body { width: 1200px; height: 871px; overflow: hidden; background: var(--white); }
  body { position: relative; font-family: "Arimo", Arial, sans-serif; color: var(--text); }
  .abs { position: absolute; }

  /* header */
  .brand { left: 84px; top: 96px; font-size: 64px; font-weight: 700; color: var(--ink); letter-spacing: -1px; line-height: 1; }
  .rss { left: 272px; top: 170px; font-size: 11px; font-weight: 700; color: var(--ink); letter-spacing: .5px; }
  .topnav { left: 596px; top: 82px; display: flex; gap: 0; height: 40px; align-items: center; }
  .topnav a { font-size: 21px; color: var(--ink); text-decoration: none; padding: 8px 12px; }
  .topnav a.active { background: var(--green); color: var(--white); }
  .header-rule { left: 570px; top: 125px; width: 546px; height: 1px; background: var(--panel-line); }
  .search-field { left: 744px; top: 156px; width: 264px; height: 24px; background: var(--search); }
  .search-btn { left: 1018px; top: 154px; width: 86px; height: 28px; background: var(--green); color: var(--white); font-size: 14px; text-align: center; line-height: 28px; }

  /* sidebar */
  .side-section { left: 104px; font-size: 25px; color: var(--ink); }
  .side-active { left: 96px; top: 316px; width: 156px; height: 33px; background: var(--green); color: var(--white); font-size: 25px; padding-left: 8px; line-height: 33px; }
  .side-active::after { content: ""; position: absolute; right: -12px; top: 0; border-left: 12px solid var(--green); border-top: 16.5px solid transparent; border-bottom: 16.5px solid transparent; }
  .submenu { left: 110px; top: 364px; list-style: none; }
  .submenu li { font-size: 12px; line-height: 17.6px; color: var(--text); }
  .submenu li.current::before { content: "› "; color: var(--green-dark); }

  /* main panel */
  .panel { left: 257px; top: 223px; width: 523px; height: 473px; background: var(--panel); }
  .crumb { left: 272px; top: 240px; font-size: 12px; color: var(--text); }
  .crumb b { color: var(--green-dark); font-weight: 400; }
  .calc { left: 276px; top: 267px; width: 492px; height: 280px; background: var(--white); border: 1px solid var(--panel-line); }
  .calc-title { left: 296px; top: 286px; font-size: 17px; color: var(--ink); }
  .calc-badge { left: 718px; top: 272px; }
  .form { left: 290px; top: 326px; width: 468px; }
  .select { height: 20px; border: 1px solid #999; font-size: 11px; padding-left: 6px; line-height: 18px; margin-left: 182px; width: 282px; position: relative; }
  .row { display: flex; align-items: center; height: 20.6px; font-size: 11px; }
  .row .label { width: 236px; }
  .row .value { width: 80px; }
  .row .btn { width: 110px; height: 17px; border: 1px solid #999; border-radius: 3px; background: linear-gradient(#fff, #e2e2e2); text-align: center; font-size: 10.5px; line-height: 15px; }
  .label-only { font-size: 11px; height: 20.6px; line-height: 20.6px; }
  .summary { left: 276px; top: 552px; width: 492px; height: 136px; background: var(--green-pale); }
  .summary-head { left: 286px; top: 562px; font-size: 12px; font-weight: 700; color: var(--ink); }
  .summary-text { left: 286px; top: 590px; width: 460px; font-size: 11px; line-height: 15px; color: var(--ink); }
  .action { top: 652px; height: 30px; background: var(--green); color: var(--white); font-size: 14px; text-align: center; line-height: 30px; border-radius: 2px; }

  /* ads */
  .ad-sound { left: 804px; top: 223px; width: 300px; height: 250px; background: var(--ad-dark); overflow: hidden; }
  .ad-sound .art { position: absolute; left: 130px; top: 70px; width: 170px; height: 180px; background: radial-gradient(circle at 55% 50%, #4a4a4a, #161616 70%); }
  .ad-sound .name { position: absolute; left: 18px; top: 30px; font-size: 30px; font-weight: 700; color: var(--white); letter-spacing: -1px; }
  .ad-sound .dot { position: absolute; left: 18px; top: 18px; width: 10px; height: 10px; background: var(--green); }
  .ad-sound .tag { position: absolute; left: 18px; top: 170px; font-size: 13px; font-style: italic; color: var(--white); line-height: 17px; }
  .ad-sound .tag b { color: var(--green); font-weight: 400; }
  .ad-sound .bar { position: absolute; left: 0; bottom: 0; width: 100%; height: 6px; background: var(--green); }
  .ad-relax { left: 804px; top: 480px; width: 300px; height: 250px; background: linear-gradient(180deg, #8fc7ea 0%, #bfe0f2 45%, #e7d9a8 75%, #c9b67a 100%); border: 1px solid #bbb; }
  .ad-relax .title { position: absolute; right: 14px; top: 30px; font-size: 31px; font-weight: 700; color: var(--white); background: #e08a12; padding: 2px 8px; }
  .ad-relax .note { position: absolute; left: 12px; bottom: 12px; width: 274px; background: var(--white); padding: 6px 8px; font-size: 9px; line-height: 12px; color: var(--ink); }
  .ad-relax .note .site { color: #e08a12; font-weight: 700; float: right; }

  /* footer */
  .footer-rule { left: 96px; top: 764px; width: 1008px; height: 1px; background: var(--panel-line); }
  .foot-col { top: 790px; font-size: 11px; line-height: 16px; color: var(--ink); list-style: none; }
  .foot-col .lead { color: var(--green-dark); font-weight: 700; }
  .copyright { right: 96px; top: 790px; font-size: 11px; color: var(--ink); }
  .socials { left: 550px; top: 816px; display: flex; gap: 26px; }
  .socials span { width: 32px; height: 32px; background: var(--social); display: block; }
</style>
</head>
<body>
  <header>
    <div class="abs brand">Sumworks.co.uk</div>
    <div class="abs rss">RSS FEED</div>
    <nav class="abs topnav">
      <a href="#">Pregnancy</a><a href="#">Health</a><a href="#" class="active">Finance</a><a href="#">Math</a><a href="#">Conversion</a>
    </nav>
    <div class="abs header-rule"></div>
    <div class="abs search-field"></div>
    <div class="abs search-btn">search</div>
  </header>

  <aside>
    <div class="abs side-section" style="top:244px">Pregnancy</div>
    <div class="abs side-section" style="top:282px">Health</div>
    <div class="abs side-active">Finance</div>
    <ul class="abs submenu">
      <li>Mortgage Calculator</li>
      <li>Retirement Calculator</li>
      <li class="current">Tax Calculator</li>
      <li>Loan Calculator</li>
      <li>Personal Finance</li>
      <li>Investment Calculator</li>
      <li>Savings Calculator</li>
      <li>Insurance Calculator</li>
    </ul>
    <div class="abs side-section" style="top:568px">Math</div>
    <div class="abs side-section" style="top:604px">Conversion</div>
  </aside>

  <main>
    <div class="abs panel"></div>
    <div class="abs crumb">Home &gt; Finance &gt; <b>Tax Calculator</b></div>
    <div class="abs calc"></div>
    <div class="abs calc-title">Tax Calculator for 2011</div>
    <svg class="abs calc-badge" width="46" height="40" viewBox="0 0 46 40"><path d="M0 0H46V40C30 40 10 30 0 0Z" fill="#7dc21e"/><circle cx="30" cy="16" r="8" fill="none" stroke="#fff" stroke-width="3"/></svg>
    <div class="abs form">
      <div class="row"><span class="label" style="width:182px">Filing status:</span></div>
      <div class="select" style="margin-top:-20px">Single
        <svg style="position:absolute;right:6px;top:6px" width="8" height="6"><path d="M0 0H8L4 6Z" fill="#333"/></svg></div>
      <div class="row"><span class="label">Total exemptions:</span><span class="value">0</span><span class="btn">Exemptions</span></div>
      <div class="row"><span class="label">Total income:</span><span class="value">$50,000</span><span class="btn">Income</span></div>
      <div class="row"><span class="label">Total adjustments:</span><span class="value">$0</span><span class="btn">Adjustments</span></div>
      <div class="row"><span class="label">Adjusted gross income:</span><span class="value">$50,000</span><span class="btn">Deductions</span></div>
      <div class="row"><span class="label">Taxable income:</span><span class="value">$44,200</span></div>
      <div class="row"><span class="label">Total credits:</span><span class="value">$0</span><span class="btn">Tax Credits</span></div>
      <div class="row"><span class="label">Total tax:</span><span class="value">$7,175</span><span class="btn">Other Taxes</span></div>
      <div class="row"><span class="label">Total payments and refundable credits:</span><span class="value">$0</span><span class="btn">Tax Payments</span></div>
    </div>
    <div class="abs summary"></div>
    <div class="abs summary-head">Your taxes are estimated at $7,175.</div>
    <p class="abs summary-text">This is 14.35% of your total income of $50,000. Your total tax payments for the year were $0. Your outstanding tax bill is estimated at $7,175. This puts you in the 25.00% tax bracket.</p>
    <div class="abs action" style="left:566px;width:88px">calculate</div>
    <div class="abs action" style="left:662px;width:96px">view report</div>
  </main>

  <aside>
    <div class="abs ad-sound">
      <div class="art" role="img" aria-label="Studio headphones on a dark background"></div>
      <span class="dot"></span>
      <div class="name">SOUNDGROVE</div>
      <div class="tag">Your Choice for<br><b>Music Loops &amp;<br>Sound Effects</b></div>
      <div class="bar"></div>
    </div>
    <div class="abs ad-relax" role="img" aria-label="Tropical beach with palm trees and a sun lounger">
      <div class="title">Go Unwind</div>
      <div class="note">Go on, book today and give yourself a calm break with a beautiful seaside view. <span class="site">gounwind.com</span><br>Enter Site for more Details</div>
    </div>
  </aside>

  <footer>
    <div class="abs footer-rule"></div>
    <ul class="abs foot-col" style="left:128px"><li class="lead">About PlotMeadow</li><li>Contact Us</li><li>Press Releases</li></ul>
    <ul class="abs foot-col" style="left:268px"><li>Portfolio</li><li>Domains</li><li>Advertising</li></ul>
    <ul class="abs foot-col" style="left:396px"><li>Expertise</li><li>Opportunities</li><li>Careers</li></ul>
    <div class="abs copyright">© 2011 PlotMeadow Net Ltd</div>
    <div class="abs socials"><span></span><span></span><span></span><span></span><span></span><span></span><span></span><span></span></div>
  </footer>
</body>
</html>
```